Cover Frontier is a rock band playing our versions of classic songs from the 70's, 80's & 90's. We are enthusiastic and competent musicians with a special emphasis on Australian rock. W
We play mostly in and around Sydney & love parties and weddings. We will travel to country venues for special events or festivals.

```html
<!DOCTYPE html>
<html lang="en">
<head>
<meta charset="utf-8">
<title>Cover Frontier – Flyer</title>
<link href="https://fonts.googleapis.com/css2?family=Oswald:wght@500;600&family=Kaushan+Script&family=Open+Sans:wght@600&display=swap" rel="stylesheet">
<style>
  :root{
    --bg:#e9ebed;
    --teal:#1f7a78;
    --red:#e2452c;
    --white:#ffffff;
    --sky-top:#eef4fb;
    --sky-mid:#7fa6d4;
    --crowd:#1b2638;
    --night:#0b0f18;
  }
  *{margin:0;padding:0;box-sizing:border-box}
  html,body{width:1200px;height:1000px;overflow:hidden;background:var(--bg)}
  .canvas{position:relative;width:1200px;height:1000px}
  .flyer{
    position:absolute;left:270px;top:60px;width:660px;height:880px;overflow:hidden;
    box-shadow:0 10px 30px rgba(0,0,0,.25);
  }
  .flyer__photo{
    position:absolute;inset:0;
    background:linear-gradient(180deg,var(--sky-top) 0%,#dfe9f5 28%,var(--sky-mid) 48%,#3d5a86 60%,var(--crowd) 74%,var(--night) 100%);
  }
  .flyer__mic{
    position:absolute;left:215px;top:14px;width:200px;height:140px;border-radius:40px;
    background:radial-gradient(ellipse at center,rgba(31,122,120,.55),rgba(31,122,120,0) 70%);
  }
  .flyer__flourish{
    position:absolute;width:110px;height:26px;border-radius:13px;
    background:rgba(226,69,44,.35);
  }
  .flourish--tl{left:110px;top:110px}
  .flourish--tr{left:440px;top:110px}
  .flourish--bl{left:110px;top:402px}
  .flourish--br{left:440px;top:402px}
  .band-name{
    position:absolute;left:0;right:0;top:170px;text-align:center;
    font-family:"Oswald",sans-serif;font-weight:600;font-size:76px;line-height:90px;
    color:var(--teal);letter-spacing:6px;
  }
  .headline{
    position:absolute;left:0;right:0;text-align:center;color:var(--red);
    font-family:"Oswald",sans-serif;font-weight:500;
  }
  .headline--songs{top:446px;font-size:46px;letter-spacing:7px}
  .headline--decades{top:500px;font-size:56px;letter-spacing:6px}
  .headline--decades small{font-size:38px}
  .invite{
    position:absolute;left:0;right:0;top:606px;text-align:center;color:var(--white);
    font-family:"Kaushan Script",cursive;font-size:34px;line-height:40px;letter-spacing:3px;
  }
  .cta{
    position:absolute;left:0;right:0;top:718px;text-align:center;color:var(--red);
    font-family:"Oswald",sans-serif;font-weight:600;font-size:70px;line-height:90px;letter-spacing:8px;
  }
  .contact{
    position:absolute;bottom:18px;display:flex;align-items:center;gap:12px;
    font-family:"Open Sans",sans-serif;font-weight:600;font-size:15px;color:var(--red);letter-spacing:1px;
  }
  .contact--web{left:18px}
  .contact--phone{right:24px;color:var(--white)}
  .contact__dot{width:42px;height:42px;border-radius:50%;background:var(--white);display:flex;align-items:center;justify-content:center}
</style>
</head>
<body>
<div class="canvas">
  <article class="flyer">
    <div class="flyer__photo" role="img" aria-label="Concert crowd with raised hands under bright blue stage lights"></div>
    <div class="flyer__mic" role="img" aria-label="Microphone on a stand illustration with two stars"></div>
    <div class="flyer__flourish flourish--tl" role="img" aria-label="Decorative red swirl"></div>
    <div class="flyer__flourish flourish--tr" role="img" aria-label="Decorative red swirl"></div>
    <h1 class="band-name">COVER<br>FRONTIER</h1>
    <div class="flyer__flourish flourish--bl" role="img" aria-label="Decorative red swirl"></div>
    <div class="flyer__flourish flourish--br" role="img" aria-label="Decorative red swirl"></div>
    <p class="headline headline--songs">CLASSIC SONGS FROM</p>
    <p class="headline headline--decades">70'S <small>TO</small> 90'S!</p>
    <p class="invite">Invite us to your<br>parties &amp; weddings</p>
    <p class="cta">CALL US NOW!</p>
    <div class="contact contact--web">
      <span class="contact__dot"></span>
      <span>www.coverfrontierband.net</span>
    </div>
    <div class="contact contact--phone">
      <span class="contact__dot">
        <svg width="24" height="24" viewBox="0 0 24 24" aria-hidden="true">
          <path fill="#e2452c" d="M6.6 10.8a15.1 15.1 0 0 0 6.6 6.6l2.2-2.2a1 1 0 0 1 1-.25 11.4 11.4 0 0 0 3.6.57 1 1 0 0 1 1 1V20a1 1 0 0 1-1 1A17 17 0 0 1 3 4a1 1 0 0 1 1-1h3.5a1 1 0 0 1 1 1c0 1.25.2 2.45.57 3.57a1 1 0 0 1-.25 1z"/>
        </svg>
      </span>
      <span>putnumberhere</span>
    </div>
  </article>
</div>
</body>
</html>
```